BRISKWAY traffic management plans

The preparation of traffic management plans for architects, builders, landscapers for council approval. The preparation of the plans can include submitting to council, briefing the builder regarding management of the plan, onsite visit, taking photographs, measurements and establishing the best outcome. Implementing the plan can also take place if need be.
NO EXISTING LOGO AVAILABLE
No photos or documents available to upload

Target Market(s)

Builders, architects, landscapers
No existing logo availalble

Industry/Entity Type

Builders

Contact Information for Business Card

BRISKWAY Traffic Management Plans
Tom Brindley
harbourlane@zentrynet.com.au
0427 693 058

Font styles to use
Serif

Colors
1b1b1b

Requirements
Must have
• competitive prices
• No existing logo available
• No photos available
Nice to have
• Black with orange and white
• No existing logo available no
Should not have
• no existing logo available
• No photos or documents to upload

```html
<!DOCTYPE html>
<html lang="en">
<head>
<meta charset="utf-8">
<title>BRISKWAY Traffic Management Plans – Business Card</title>
<link href="https://fonts.googleapis.com/css2?family=Raleway:wght@300;400;800&display=swap" rel="stylesheet">
<style>
  :root {
    --backdrop: #d9d9d9;
    --card: #1b1b1b;
    --white: #f2f2f2;
    --grey: #a8a8a8;
    --orange: #e0712c;
  }
  * { margin: 0; padding: 0; box-sizing: border-box; }
  html, body {
    width: 1200px;
    height: 800px;
    overflow: hidden;
    background: var(--backdrop);
  }
  .canvas {
    position: relative;
    width: 1200px;
    height: 800px;
    display: flex;
    align-items: center;
    justify-content: center;
  }
  .business-card {
    position: relative;
    width: 960px;
    height: 560px;
    background: var(--card);
    border-radius: 40px;
    font-family: "Raleway", sans-serif;
    color: var(--white);
    box-shadow: 0 20px 40px rgba(0,0,0,0.25);
  }
  .brand {
    position: absolute;
    left: 170px;
    top: 110px;
  }
  .brand-name {
    display: flex;
    align-items: center;
    gap: 18px;
    font-weight: 800;
    font-size: 112px;
    line-height: 1;
    letter-spacing: -2px;
    color: var(--white);
  }
  .brand-mark {
    width: 34px;
    height: 34px;
    background: var(--orange);
    flex: none;
  }
  .brand-tagline {
    margin-top: 14px;
    font-weight: 400;
    font-size: 30px;
    letter-spacing: 8px;
    text-transform: uppercase;
    color: var(--grey);
  }
  .rule {
    position: absolute;
    height: 2px;
    background: var(--orange);
  }
  .rule-top { left: 170px; right: 70px; top: 300px; }
  .rule-bottom { left: 170px; right: 360px; top: 420px; }
  .holder-name {
    position: absolute;
    left: 166px;
    top: 318px;
    font-weight: 400;
    font-size: 80px;
    line-height: 1;
    color: var(--white);
  }
  .contact-list {
    position: absolute;
    left: 184px;
    top: 442px;
    list-style: none;
  }
  .contact-item {
    display: flex;
    align-items: center;
    gap: 10px;
    font-weight: 400;
    font-size: 30px;
    line-height: 44px;
    color: var(--white);
  }
  .contact-icon { width: 28px; height: 28px; flex: none; }
</style>
</head>
<body>
  <main class="canvas">
    <section class="business-card" aria-label="Business card">
      <div class="brand">
        <div class="brand-name"><span class="brand-mark"></span>BRISKWAY</div>
        <div class="brand-tagline">Traffic Management Plans</div>
      </div>

      <div class="rule rule-top"></div>
      <h1 class="holder-name">Tom Brindley</h1>
      <div class="rule rule-bottom"></div>

      <ul class="contact-list">
        <li class="contact-item">
          <svg class="contact-icon" viewBox="0 0 28 28" aria-hidden="true">
            <circle cx="14" cy="14" r="12" fill="none" stroke="var(--orange)" stroke-width="2"/>
            <path d="M10 8 l3 0 l1 4 l-2 1.5 a8 8 0 0 0 3.5 3.5 l1.5 -2 l4 1 l0 3 a2 2 0 0 1 -2 2 a12 12 0 0 1 -11 -11 a2 2 0 0 1 2 -2z" fill="var(--orange)"/>
          </svg>
          <span>0427 693 058</span>
        </li>
        <li class="contact-item">
          <svg class="contact-icon" viewBox="0 0 28 28" aria-hidden="true">
            <rect x="2" y="6" width="24" height="16" fill="none" stroke="var(--orange)" stroke-width="2"/>
            <path d="M2 6 L14 16 L26 6 M2 22 L11 13.5 M26 22 L17 13.5" fill="none" stroke="var(--orange)" stroke-width="2"/>
          </svg>
          <span>harbourlane@zentrynet.com.au</span>
        </li>
      </ul>
    </section>
  </main>
</body>
</html>
```